Discover Your Own Mortgage Qualifications from Your Home Computer

Target Market(s)

Consumers Looking to Purchase a Home

Industry/Entity Type

Housing Industry and Credit Score Counseling

Requirements
Must have
• The Logo, and the QR Codes, and the written text stating that Bright Ledger Path is operated by Harbor Oak Lending, a 401 (c)(3) nonprofit credit counselor
Nice to have
• The four outlines with the explanations

```html
<!DOCTYPE html>
<html lang="en">
<head>
<meta charset="utf-8">
<title>Bright Ledger Path Flyer</title>
<link rel="stylesheet" href="https://fonts.googleapis.com/css2?family=Lato:wght@400;700;900&display=swap">
<style>
  :root {
    --blue-deep: #1b3a8c;
    --blue: #2a55b8;
    --blue-head: #1f3b9c;
    --charcoal: #2b2b2d;
    --row-grey: #f0f0f0;
    --text: #4a4a4a;
    --page: #e9e9ea;
    --white: #ffffff;
  }
  * { box-sizing: border-box; margin: 0; padding: 0; }
  html, body { width: 1200px; height: 800px; overflow: hidden; }
  body { background: var(--page); font-family: "Lato", sans-serif; position: relative; }

  .flyer {
    position: absolute; left: 306px; top: 20px;
    width: 587px; height: 760px; background: var(--white);
    box-shadow: 0 4px 16px rgba(0,0,0,.18); overflow: hidden;
  }

  .hero { position: relative; height: 270px; }
  .hero svg { position: absolute; inset: 0; }
  .hero-title {
    position: absolute; left: 23px; top: 76px;
    color: var(--white); font-weight: 700; font-size: 31px; letter-spacing: -0.3px;
  }
  .hero-sub {
    position: absolute; left: 23px; top: 126px;
    color: var(--white); font-weight: 700; font-size: 14.5px; line-height: 19px;
  }

  .feature {
    position: relative; display: flex; align-items: center;
    padding: 0 18px 0 22px; gap: 16px;
  }
  .feature.alt { background: var(--row-grey); }
  .feature-icon { flex: 0 0 54px; width: 54px; height: 54px; }
  .feature-heading {
    color: var(--blue-head); font-weight: 900; font-size: 12.5px; line-height: 16px;
    text-transform: uppercase; margin-bottom: 3px;
  }
  .feature-body { color: var(--text); font-size: 10.3px; line-height: 12.6px; text-align: justify; }

  .footer { position: relative; height: 142px; }
  .footer svg.footer-bands { position: absolute; inset: 0; }
  .footer-note {
    position: absolute; left: 0; width: 480px; top: 14px; text-align: right;
    font-size: 8.6px; color: var(--charcoal);
  }
  .footer-contact {
    position: absolute; left: 23px; top: 88px;
    color: var(--white); font-size: 9.6px; line-height: 16px;
  }
  .agent { position: absolute; left: 386px; top: 82px; color: var(--white); }
  .agent-name { font-size: 19px; line-height: 22px; }
  .agent-role { font-size: 10.5px; line-height: 15px; }
  .agent-phone { font-size: 12px; font-weight: 700; line-height: 18px; display: flex; align-items: center; gap: 5px; }
</style>
</head>
<body>
<main class="flyer">
  <header class="hero">
    <svg width="587" height="270" viewBox="0 0 587 270">
      <defs>
        <linearGradient id="heroBlue" x1="0" y1="0" x2="1" y2="1">
          <stop offset="0" stop-color="#2f5cc0"/>
          <stop offset="1" stop-color="#1b3a8c"/>
        </linearGradient>
        <linearGradient id="familyTone" x1="0" y1="0" x2="1" y2="1">
          <stop offset="0" stop-color="#c9d3e6"/>
          <stop offset="0.5" stop-color="#a7b7d4"/>
          <stop offset="1" stop-color="#6f89bd"/>
        </linearGradient>
      </defs>
      <rect width="587" height="270" fill="url(#heroBlue)"/>
      <rect x="60" y="0" width="340" height="250" fill="#ffffff" opacity="0.07" role="img" aria-label="Faded photo of a suburban house"/>
      <polygon points="230,270 587,236 587,270" fill="var(--charcoal)"/>
      <path d="M318,270 C322,190 350,150 395,120 C420,60 470,25 510,40 C545,45 575,90 587,130 L587,270 Z" fill="url(#familyTone)" opacity="0.9" role="img" aria-label="Photo of a smiling family sitting together around a laptop"/>
    </svg>
    <h1 class="hero-title">BRIGHT LEDGER PATH</h1>
    <p class="hero-sub">Discover Your Own Mortgage Qualifications<br>from Your Home Computer</p>
  </header>

  <section class="feature" style="height:88px">
    <svg class="feature-icon" viewBox="0 0 54 54">
      <circle cx="27" cy="27" r="26" fill="none" stroke="#c9ccd3" stroke-width="2"/>
      <circle cx="27" cy="27" r="21" fill="var(--blue-deep)"/>
      <path d="M18,26 L26,19 L34,26 V34 H18 Z" fill="#fff"/>
      <circle cx="29" cy="28" r="5" fill="var(--blue-deep)" stroke="#fff" stroke-width="2"/>
      <line x1="32.5" y1="31.5" x2="37" y2="36" stroke="#fff" stroke-width="2.5" stroke-linecap="round"/>
    </svg>
    <div>
      <h2 class="feature-heading">Discover your mortgage qualifications FHA, Conv., VA, USDA</h2>
      <p class="feature-body">Since BLP has your lender’s Classic Veritor Scores, you can discover your potential mortgage qualifications, interest rate and monthly payment - available through Bright Ledger Path.</p>
    </div>
  </section>

  <section class="feature alt" style="height:86px">
    <svg class="feature-icon" viewBox="0 0 54 54">
      <circle cx="27" cy="27" r="26" fill="none" stroke="#c9ccd3" stroke-width="2"/>
      <circle cx="27" cy="27" r="21" fill="var(--blue-deep)"/>
      <path d="M16,27 L26,18 L36,27 H33 V36 H19 V27 Z" fill="#fff"/>
      <circle cx="27" cy="28" r="3" fill="var(--blue-deep)"/>
      <path d="M22,36 C22,32 32,32 32,36 Z" fill="var(--blue-deep)"/>
    </svg>
    <div>
      <h2 class="feature-heading">Get a ‘Lender’s Credit Report’ and find out your lender’s<br>3 Veritor® (Classic) Scores</h2>
      <p class="feature-body">Access the same credit report and the 3 ‘Classic Veritor Scores’ used by most lenders. Don’t be confused by any credit score – because there are dozens, are different and they are considered unreliable.</p>
    </div>
  </section>

  <section class="feature" style="height:86px">
    <svg class="feature-icon" viewBox="0 0 54 54">
      <circle cx="27" cy="27" r="26" fill="none" stroke="#c9ccd3" stroke-width="2"/>
      <circle cx="27" cy="27" r="21" fill="var(--blue-deep)"/>
      <rect x="24" y="15" width="14" height="18" fill="#fff"/>
      <rect x="27" y="26" width="2" height="5" fill="var(--blue-deep)"/>
      <rect x="30" y="23" width="2" height="8" fill="var(--blue-deep)"/>
      <rect x="33" y="20" width="2" height="11" fill="var(--blue-deep)"/>
      <circle cx="23" cy="30" r="6" fill="var(--blue-deep)" stroke="#fff" stroke-width="2"/>
      <line x1="19" y1="34" x2="15" y2="38" stroke="#fff" stroke-width="2.5" stroke-linecap="round"/>
    </svg>
    <div>
      <h2 class="feature-heading">Your credit report will be analyzed for score improvement</h2>
      <p class="feature-body">Bright Ledger Path reviews each account in your credit report for balances, late payments, types of accounts and lenders, credit limits and initial loan amounts, when each account was opened, closed accounts, and hard inquiries.</p>
    </div>
  </section>

  <section class="feature alt" style="height:86px">
    <svg class="feature-icon" viewBox="0 0 54 54">
      <circle cx="27" cy="27" r="26" fill="none" stroke="#c9ccd3" stroke-width="2"/>
      <circle cx="27" cy="27" r="21" fill="var(--blue-deep)"/>
      <rect x="16" y="18" width="22" height="15" fill="none" stroke="#fff" stroke-width="2"/>
      <rect x="20" y="26" width="2.5" height="4" fill="#fff"/>
      <rect x="24" y="24" width="2.5" height="6" fill="#fff"/>
      <rect x="28" y="22" width="2.5" height="8" fill="#fff"/>
      <rect x="32" y="21" width="2.5" height="9" fill="#fff"/>
      <rect x="22" y="35" width="10" height="2" fill="#fff"/>
    </svg>
    <div>
      <h2 class="feature-heading">Bright Ledger Path ranks number 1!</h2>
      <p class="feature-body">With this detailed analysis, Bright Ledger Path will provide you a step-by-step plan to improve your Classic Veritor Scores. Active clients with Bright Ledger Path have an average of an 81-point improvement.</p>
    </div>
  </section>

  <footer class="footer">
    <svg class="footer-bands" width="587" height="142" viewBox="0 0 587 142">
      <defs>
        <linearGradient id="footBlue" x1="0" y1="1" x2="1" y2="0">
          <stop offset="0" stop-color="#2a55b8"/>
          <stop offset="1" stop-color="#1b3a8c"/>
        </linearGradient>
        <linearGradient id="agentTone" x1="0" y1="0" x2="0" y2="1">
          <stop offset="0" stop-color="#c9a98e"/>
          <stop offset="0.45" stop-color="#8a7565"/>
          <stop offset="1" stop-color="#2e2e33"/>
        </linearGradient>
      </defs>
      <polygon points="0,50 420,104 420,142 0,142" fill="var(--charcoal)"/>
      <polygon points="232,142 330,74 587,20 587,142" fill="url(#footBlue)"/>
      <rect x="495" y="6" width="92" height="136" fill="url(#agentTone)" opacity="0.9" role="img" aria-label="Portrait photo of the credit score expert"/>
    </svg>
    <p class="footer-note">Bright Ledger Path is Managed by Harbor Oak Lending, a 401 (c)(3) Nonprofit Certified Credit Counselor.</p>
    <div class="footer-contact">
      <p>Harbor Oak Lending</p>
      <p>Email: Support@BrightLedgerPath.org</p>
      <p>Tel: (877) 555-0142</p>
    </div>
    <div class="agent">
      <p class="agent-name">Dale Renner</p>
      <p class="agent-role">Credit Score Expert</p>
      <p class="agent-phone">
        <svg width="11" height="13" viewBox="0 0 11 13"><rect x="1" y="0.5" width="9" height="12" rx="1.5" fill="none" stroke="#fff" stroke-width="1.5"/><rect x="3.5" y="9.5" width="4" height="1.2" fill="#fff"/></svg>
        (801) 555-0178
      </p>
    </div>
  </footer>
</main>
</body>
</html>
```